Wordpress Design Project for Employee Communications Site

We need a Wordpress design for a company that strategizes on and produces materials for employee communications. Improving employee communications at all levels of an organization can help improve overall company performance and results. The site needs to look very clean and professional; we're not afraid of white space. We like the functionality that Wordpress provides; however, we only want one "true" blog page; the other pages should give the impression of a more "static" web site - particularly the home page. I have a logo that I can provide.

I have added these comments to the discussion page:
Great question - thank you for asking it. I’ve done more research

I like the very clean and monochromatic looks to many of these. I don’t have to have monochromatic, but I do like minimal colors. Simple, clean, organized. The home page should “fit” almost entirely without scrolling. I do like fat footers that you can scroll down to. I don’t want a colored background, but any that I’ve chosen with colored backgrounds could be switched to a white background.

http://www.moravelkinst.com/
http://pondrix.com/
http://v1.belmarquist.com/
http://howtheotter.com/
http://stayingnimble.com/
http://www.interiors.pelmun.co.uk/
http://brixalumnihub.com/

These last two are more corporate sites. The first one is from a well-respected consultant in my area who does a lot of what I do. And I think Harwick does a nice job with their site. So, I want to marry the look I like with getting the content job done.

http://www.messagefuelworks.com/
http://www.harwick.com/view/en_US/us/index.htm

Target Market(s)

Target market is mid- to large-sized companies. More than 500 employees.

Industry/Entity Type

Communications

Requirements
Must have
• Need an impactful home page. There should be a "blog" page; contact us; services; about. For starters, at least. I want fonts to be very readable - that is, either quite dark gray or black.
Nice to have
• I am loathe to include a picture of myself, but I do want some images that say, "professional" and "expert" in communications.
Should not have
• I don't want a hits counter :) (I know no one would do that!).

```html
<!DOCTYPE html>
<html lang="en">
<head>
<meta charset="utf-8">
<title>Tessary Workplace Messaging</title>
<link rel="stylesheet" href="https://fonts.googleapis.com/css2?family=Source+Sans+3:wght@300;400;600;700&family=Arimo:wght@400&display=swap">
<style>
  :root {
    --white: #ffffff;
    --ink: #2b2b2b;
    --body: #3a3a3a;
    --rule: #8c8c8c;
    --accent-blue: #2aa6df;
    --title-blue: #1b8fca;
    --lime: #bfd63a;
    --lime-soft: #dfe9a6;
    --frame: #e4e4e4;
    --footer-bg: #f1f1f1;
    --footer-line: #c9c9c9;
    --social: #8fa3b3;
    --photo-light: #eef1f4;
    --photo-mid: #c9ced6;
    --photo-dark: #1c1d22;
  }
  * { box-sizing: border-box; margin: 0; padding: 0; }
  html, body { width: 1200px; height: 850px; overflow: hidden; background: var(--white); }
  body { position: relative; font-family: "Arimo", Arial, sans-serif; color: var(--ink); }
  a { color: inherit; text-decoration: none; }

  /* Header */
  .brand { position: absolute; left: 85px; top: 30px; display: flex; align-items: center; gap: 14px; }
  .brand-dot { width: 58px; height: 58px; border-radius: 50%; background: var(--accent-blue); }
  .brand-name { font-family: "Source Sans 3", sans-serif; font-weight: 400; font-size: 32px; color: var(--lime); }

  .main-nav { position: absolute; left: 0; top: 115px; width: 1200px; height: 30px; }
  .main-nav::before, .main-nav::after { content: ""; position: absolute; top: 13px; height: 3px; background: var(--rule); }
  .main-nav::before { left: 0; width: 666px; }
  .main-nav::after { left: 1042px; right: 0; }
  .nav-list { position: absolute; left: 666px; top: 0; display: flex; list-style: none; }
  .nav-item { font-family: "Source Sans 3", sans-serif; font-weight: 300; font-size: 20px; color: var(--ink); padding: 0 17px; line-height: 24px; border-left: 1px solid var(--ink); position: relative; }
  .nav-item:first-child { border-left: none; padding-left: 9px; }
  .nav-item.is-current { color: var(--accent-blue); }
  .nav-item.is-current svg { position: absolute; left: 28px; top: 26px; }

  /* Hero */
  .hero { position: absolute; left: 75px; top: 162px; width: 1045px; height: 222px; border: 1px solid var(--frame); padding: 6px; display: flex; gap: 5px; }
  .hero-panel { width: 361px; height: 208px; background: var(--lime); padding: 10px 8px 0 14px; font-family: "Source Sans 3", sans-serif; font-weight: 400; font-size: 28.5px; line-height: 35px; color: var(--ink); white-space: nowrap; }
  .hero-panel strong { font-weight: 600; color: var(--white); }
  .hero-photo { flex: 1; height: 208px; background: linear-gradient(90deg, var(--photo-light) 0%, var(--photo-mid) 55%, #8d939c 85%, var(--photo-dark) 100%); }

  /* Features */
  .features { position: absolute; left: 142px; top: 421px; width: 960px; display: grid; grid-template-columns: 332px 342px 286px; row-gap: 26px; }
  .feature { display: flex; gap: 10px; }
  .feature-mark { width: 30px; height: 30px; flex: none; margin-top: 8px; border-radius: 50%; background: var(--lime-soft); }
  .feature-title { font-family: "Source Sans 3", sans-serif; font-weight: 600; font-size: 15px; color: var(--title-blue); line-height: 18px; }
  .feature-text { font-size: 11.5px; line-height: 14.5px; color: var(--body); width: 215px; }

  /* Footer */
  .site-footer { position: absolute; left: 0; top: 616px; width: 1200px; height: 188px; background: var(--footer-bg); border-top: 1px solid #e2e2e2; }
  .footer-divider { position: absolute; top: 14px; width: 1px; height: 134px; background: var(--footer-line); }
  .footer-col { position: absolute; top: 16px; }
  .footer-heading { font-family: "Source Sans 3", sans-serif; font-weight: 600; font-size: 15px; color: var(--ink); line-height: 18px; margin-bottom: 6px; }
  .footer-links { list-style: none; }
  .footer-links li { font-size: 11.5px; line-height: 19.6px; letter-spacing: 0.4px; color: var(--ink); }
  .social { display: flex; gap: 6px; margin-top: 8px; }
  .social span { width: 17px; height: 17px; background: var(--social); display: block; }
  .copyright { position: absolute; left: 0; top: 818px; width: 1200px; text-align: center; padding-left: 90px; font-size: 11px; letter-spacing: 0.3px; color: var(--ink); }
</style>
</head>
<body>
  <header class="site-header">
    <div class="brand">
      <span class="brand-dot"></span>
      <span class="brand-name">Tessary Workplace Messaging</span>
    </div>
    <nav class="main-nav">
      <ul class="nav-list">
        <li class="nav-item is-current"><a href="#">works</a>
          <svg width="12" height="7" viewBox="0 0 12 7"><path d="M1 1l5 4 5-4" fill="none" stroke="#2aa6df" stroke-width="1.6"/></svg>
        </li>
        <li class="nav-item"><a href="#">process</a></li>
        <li class="nav-item"><a href="#">about</a></li>
        <li class="nav-item"><a href="#">contact</a></li>
      </ul>
    </nav>
  </header>

  <section class="hero">
    <div class="hero-panel">We help <strong>businesses</strong><br><strong>improve</strong> their<br>performance through<br>effective communication.<br>Our approach is simple</div>
    <div class="hero-photo" role="img" aria-label="Photo of business colleagues talking in a bright office"></div>
  </section>

  <section class="features">
    <article class="feature">
      <span class="feature-mark"></span>
      <div><h3 class="feature-title">Employee Packet</h3><p class="feature-text">Publish messages on desktop backgrounds. Change and sequence messages easily.</p></div>
    </article>
    <article class="feature">
      <span class="feature-mark"></span>
      <div><h3 class="feature-title">Employee Packet</h3><p class="feature-text">Publish messages on desktop backgrounds. Change and sequence messages easily.</p></div>
    </article>
    <article class="feature">
      <span class="feature-mark"></span>
      <div><h3 class="feature-title">Employee Packet</h3><p class="feature-text">Publish messages on desktop backgrounds. Change and sequence messages easily.</p></div>
    </article>
    <article class="feature">
      <span class="feature-mark"></span>
      <div><h3 class="feature-title">Employee Packet</h3><p class="feature-text">Publish messages on desktop backgrounds. Change and sequence messages easily.</p></div>
    </article>
    <article class="feature">
      <span class="feature-mark"></span>
      <div><h3 class="feature-title">Employee Packet</h3><p class="feature-text">Publish messages on desktop backgrounds. Change and sequence messages easily.</p></div>
    </article>
    <article class="feature">
      <span class="feature-mark"></span>
      <div><h3 class="feature-title">Employee Packet</h3><p class="feature-text">Publish messages on desktop backgrounds. Change and sequence messages easily.</p></div>
    </article>
  </section>

  <footer class="site-footer">
    <span class="footer-divider" style="left:245px"></span>
    <span class="footer-divider" style="left:454px"></span>
    <span class="footer-divider" style="left:680px"></span>
    <span class="footer-divider" style="left:877px"></span>
    <div class="footer-col" style="left:105px">
      <h4 class="footer-heading">Company</h4>
      <ul class="footer-links"><li>About Us</li><li>Sitemap</li><li>Website Terms</li><li>Terms of Business</li><li>Privacy Policy</li></ul>
    </div>
    <div class="footer-col" style="left:305px">
      <h4 class="footer-heading">Product</h4>
      <ul class="footer-links"><li>Business Websites</li><li>Reviews</li><li>Quick Tour</li><li>Pricing</li><li>Free Trial</li></ul>
    </div>
    <div class="footer-col" style="left:506px">
      <h4 class="footer-heading">Internet Marketing</h4>
      <ul class="footer-links"><li>Marketing Tips</li><li>Search Optimisation</li><li>Social Media</li><li>Video Marketing</li><li>Business Cases</li></ul>
    </div>
    <div class="footer-col" style="left:722px">
      <h4 class="footer-heading">Services</h4>
      <ul class="footer-links"><li>Help/Contact us</li><li>Business directory</li><li>Legal notices</li><li>Privacy policy</li><li>Terms &amp; Conditions</li></ul>
    </div>
    <div class="footer-col" style="left:911px">
      <h4 class="footer-heading">Follow us</h4>
      <div class="social" aria-label="Social links"><span></span><span></span><span></span><span></span></div>
    </div>
  </footer>
  <p class="copyright">Copyright © 2012 Tessary Workplace Messaging. All rights reserved.</p>
</body>
</html>
```